Fundraising Study Day East of England. Lift the January blues!

A flyer to advertise a fundraising event of lectures for dental hygienists and therapists in support of the exemption campaign. Currently dental hygienists and therapists require a prescription to deliver certain treatment or recommend certain toothpastes. If we are successful in the campaign we will be able to treat patients without these restrictions.

Dental

```html
<!DOCTYPE html>
<html lang="en">
<head>
<meta charset="utf-8">
<title>Fundraising Study Day East of England</title>
<link href="https://fonts.googleapis.com/css2?family=Open+Sans:ital,wght@0,400;0,700;0,800;1,400&display=swap" rel="stylesheet">
<style>
  :root {
    --teal: #007f7f;
    --yellow: #f7ee17;
    --white: #ffffff;
    --mint: #cfe8e6;
  }
  * { margin: 0; padding: 0; box-sizing: border-box; }
  html, body { width: 848px; height: 1200px; overflow: hidden; background: var(--teal); }
  .flyer {
    position: relative;
    width: 848px;
    height: 1200px;
    background: var(--teal);
    font-family: "Open Sans", Arial, sans-serif;
    color: var(--white);
    overflow: hidden;
  }
  .shapes { position: absolute; inset: 0; }
  .title {
    position: absolute;
    left: 72px;
    top: 57px;
    font-weight: 800;
    font-size: 45px;
    line-height: 60px;
    color: var(--teal);
    letter-spacing: 0.3px;
    white-space: nowrap;
  }
  .tagline {
    position: absolute;
    left: 73px;
    top: 190px;
    font-style: italic;
    font-weight: 400;
    font-size: 48px;
    letter-spacing: 7px;
    color: var(--yellow);
    white-space: nowrap;
  }
  .intro {
    position: absolute;
    left: 74px;
    top: 257px;
    font-size: 16.2px;
    line-height: 28.8px;
    letter-spacing: 0.1px;
    white-space: nowrap;
  }
  .location {
    position: absolute;
    left: 75px;
    top: 374px;
    font-weight: 700;
    font-size: 21px;
    letter-spacing: 0.2px;
    white-space: nowrap;
  }
  .date-card {
    position: absolute;
    left: 122px;
    top: 419px;
    width: 517px;
    height: 159px;
    background: var(--white);
    box-shadow: 0 8px 6px -4px rgba(0,0,0,0.35);
    color: var(--teal);
  }
  .date-card .day {
    position: absolute;
    left: 20px;
    top: -4px;
    font-weight: 800;
    font-size: 86px;
    line-height: 100px;
  }
  .date-card .date {
    position: absolute;
    left: 20px;
    top: 80px;
    font-weight: 800;
    font-size: 37.5px;
    white-space: nowrap;
  }
  .date-card .time {
    position: absolute;
    left: 32px;
    top: 130px;
    font-size: 18.5px;
  }
  .price {
    position: absolute;
    left: 608px;
    top: 412px;
    width: 180px;
    height: 180px;
    border-radius: 50%;
    background: var(--yellow);
    display: flex;
    align-items: center;
    justify-content: center;
    color: var(--teal);
    font-weight: 700;
    font-size: 33px;
  }
  .price::before {
    content: "";
    position: absolute;
    inset: 10px;
    border: 2.5px dashed var(--white);
    border-radius: 50%;
  }
  .agenda-heading {
    position: absolute;
    left: 293px;
    top: 584px;
    font-weight: 400;
    font-size: 49px;
    line-height: 60px;
    color: var(--yellow);
    letter-spacing: 0.5px;
  }
  .agenda {
    position: absolute;
    right: 68px;
    top: 622px;
    width: 660px;
    text-align: right;
    font-size: 15.8px;
    line-height: 23.75px;
  }
  .agenda .slot { color: var(--yellow); }
  .mascot {
    position: absolute;
    left: 0;
    top: 868px;
    width: 226px;
    height: 250px;
    border-radius: 40px 80px 60px 20px;
    background: linear-gradient(160deg, var(--mint), #a9d6d2);
  }
  .ticket-link {
    position: absolute;
    left: 74px;
    top: 1125px;
    font-weight: 700;
    font-size: 11.6px;
    color: var(--yellow);
    white-space: nowrap;
  }
</style>
</head>
<body>
<main class="flyer">
  <svg class="shapes" width="848" height="1200" viewBox="0 0 848 1200" aria-hidden="true">
    <polygon points="0,44 696,44 781,183 0,183" fill="var(--white)"/>
    <rect x="0" y="1162" width="848" height="38" fill="var(--white)"/>
    <polygon points="394,1162 470,1162 430,1200 432,1200" fill="var(--teal)"/>
    <polygon points="470,1162 848,1162 848,1200 436,1200" fill="var(--yellow)"/>
  </svg>

  <h1 class="title">FUNDRAISING STUDY DAY<br>EAST OF ENGLAND</h1>
  <p class="tagline">Lift the January blues!</p>
  <p class="intro">A fundraising event to support our exemptions project. The day will consist of a series of<br>presentations ranging from the new ECPD to new technologies. The aim, being to enhance<br>our learning and raise funds to support the exemptions campaign. The speaker line includes<br>some of the UK and Irelands most respected dental prefessionals in our field.</p>
  <p class="location">LOCATION : ALDER HOTEL - MILL WAY - ELMFORD - EF10 2QT</p>

  <div class="date-card">
    <div class="day">FRIDAY</div>
    <div class="date">19 JANUARY 2018</div>
    <div class="time">09:00 – 16:30 GMT</div>
  </div>
  <div class="price">£101.48</div>

  <h2 class="agenda-heading">AGENDA</h2>
  <div class="agenda">
    <span class="slot">9.30 - 10.15&nbsp; - HELEN MARLOW</span><br>
    Immediate past president of the ADTH will be updating us on all things ECPD<br>
    <span class="slot">10.15 - 11.00 - TESSA BRIGHTWELL</span><br>
    Will provide an update on teeth whiteing and explain how social media has<br>
    impacted her business<br>
    Clara Westby: Our internationally acclaimed speaker will update our<br>
    knowledge of periodontal disease and nutrition and new technologies.<br>
    <span class="slot">11.00 - 11.30&nbsp; BREAK</span><br>
    <span class="slot">11.30 - 13.00 - NIAMH CORRIGAN &amp; ROSIE TAMWORTH</span><br>
    Will be providing a combined presentation on 'Scaling your business' and start<br>
    to finish Sonivex techniques. The aim being to build our business with<br>
    effective communications, systems and protocols. This sessions promises<br>
    audience participation!<br>
    <span class="slot">12 - 1400 LUNCH</span><br>
    <span class="slot">14 - 15.00 - ANIL MEHRA</span><br>
    Save your back. All things posture.<br>
    <span class="slot">15.00 - 15.30 BREAK</span><br>
    <span class="slot">15.30 16.30&nbsp; -&nbsp; CLARA WESTBY</span><br>
    Our internationally acclaimed speaker will update our knowledge of<br>
    periodontal disease and nutrition and new technologies.
  </div>

  <div class="mascot" role="img" aria-label="Cartoon tooth mascot holding a red toothbrush and giving a thumbs up"></div>

  <p class="ticket-link">https://www.ticketbay.co.uk/e/fundraising-study-day-east-of-england-lift-the-january-blues-tickets-48213067521</p>
</main>
</body>
</html>
```